Hollow Lantern
A Derek Mowbray Mystery
Hollow Lantern - Books
Creative Brief
Book cover for the second in a four book series. First book: Winter Ledger, A Derek Mowbray Mystery, available on Bookvine. The main character, Derek Mowbray, finds a diary in a secret compartment of an old desk. The pages of the diary are spattered with blood.
Books
E-book reader of male gay erotica.
Must relate to in style to cover of first book. Use of autumn (fall) colors.
Nine Hundred Nights: A Woman's Passage within the National Probation Maze
Book Cover Design for Novel
A Borrowed Silence
Book Cover for eBook - "She Was Shaped For Gentle Light"

```html
<!DOCTYPE html>
<html lang="en">
<head>
<meta charset="utf-8">
<title>Hollow Lantern — A Derek Mowbray Mystery</title>
<link rel="stylesheet" href="https://fonts.googleapis.com/css2?family=Anton&family=Josefin+Sans:wght@400&family=Cinzel:wght@400&display=swap">
<style>
  :root {
    --page: #f1efec;
    --frame: #ffffff;
    --skin-shadow: #5e636b;
    --skin-light: #9ea3a9;
    --shirt: #cfd2d6;
    --wood-dark: #3a271d;
    --wood-mid: #5a3d2c;
    --ember: #f08a1c;
    --leaf-red: #c23a12;
    --leaf-gold: #e9b233;
    --leaf-green: #6f8a2a;
    --ink-light: #f3f1ee;
  }
  * { margin: 0; padding: 0; box-sizing: border-box; }
  html, body {
    width: 1200px;
    height: 718px;
    overflow: hidden;
    background: var(--page);
  }
  .stage {
    width: 1200px;
    height: 718px;
    display: flex;
    align-items: center;
    justify-content: center;
  }
  .book-cover {
    position: relative;
    width: 494px;
    height: 680px;
    background: var(--frame);
    padding: 10px;
    box-shadow: 0 2px 10px rgba(0,0,0,.18);
  }
  .cover-art {
    position: relative;
    width: 100%;
    height: 100%;
    overflow: hidden;
  }
  .cover-photo {
    position: absolute;
    inset: 0;
    background:
      radial-gradient(ellipse 55% 45% at 25% 80%, var(--shirt) 0%, rgba(207,210,214,0) 70%),
      radial-gradient(ellipse 60% 55% at 35% 45%, var(--skin-light) 0%, rgba(158,163,169,0) 75%),
      linear-gradient(90deg, var(--skin-shadow) 0%, var(--skin-light) 35%, var(--wood-mid) 58%, var(--wood-dark) 100%);
  }
  .cover-photo::after {
    content: "";
    position: absolute;
    inset: 0;
    background: linear-gradient(180deg, rgba(20,20,24,.55) 0%, rgba(20,20,24,0) 30%);
  }
  .title-block {
    position: absolute;
    left: 0;
    right: 0;
    top: 170px;
    text-align: center;
    white-space: nowrap;
  }
  .title-main {
    display: block;
    font-family: "Anton", "Impact", sans-serif;
    font-size: 120px;
    line-height: 1;
    letter-spacing: 2px;
    color: transparent;
    background: linear-gradient(100deg, var(--leaf-gold) 0%, var(--ember) 22%, var(--leaf-red) 40%, var(--leaf-green) 55%, var(--ember) 72%, var(--leaf-red) 100%);
    -webkit-background-clip: text;
    background-clip: text;
    -webkit-text-stroke: 1.5px rgba(255,255,255,.85);
  }
  .title-sub {
    display: block;
    margin-top: 16px;
    font-family: "Josefin Sans", "Helvetica Neue", sans-serif;
    font-size: 54px;
    line-height: 1;
    letter-spacing: 16px;
    padding-left: 16px;
    color: var(--ember);
  }
  .series-line {
    position: absolute;
    left: 0;
    right: 0;
    top: 480px;
    text-align: center;
    font-family: "Cinzel", "Times New Roman", serif;
    font-size: 19px;
    letter-spacing: 1.5px;
    color: var(--ink-light);
  }
  .author {
    position: absolute;
    left: 0;
    right: 0;
    top: 566px;
    text-align: center;
    font-family: "Cinzel", "Times New Roman", serif;
    font-size: 20px;
    letter-spacing: 2px;
    color: var(--ink-light);
  }
</style>
</head>
<body>
  <main class="stage">
    <article class="book-cover">
      <div class="cover-art">
        <div class="cover-photo" role="img" aria-label="Close-up photograph of a man's bare shoulder and neck in cool grey tones against a dark brown wooden wall"></div>
        <h1 class="title-block">
          <span class="title-main">HOLLOW</span>
          <span class="title-sub">LANTERN</span>
        </h1>
        <p class="series-line">A Derek Mowbray Mystery</p>
        <p class="author">H. Lorne</p>
      </div>
    </article>
  </main>
</body>
</html>
```